Political Mail Out Quintero front and back

Front
Esteban (9th Grade) Quintero!

What's that famous saying?

Show me who your friends are and I'll tell you who you really are!
(show the two guys)

Arturo Benavides is charged with voter fraud by changing voter addresses from across the RGV so they could vote in Edinburg
Back
Did Esteban (9th Grade) Quintero commit voter fraud when he ran for office in 2016?
(insert blurred photo)

Here is a list of people from all over the RGV that voted in Edinburg in the 2016 race.
Here is a break down:

(highlight the number and where they were first registered to vote)

9 People voted in Edinburg who were registered in Donna.
13 People voted in Edinburg who were registered in San Juan
8 People voted in Edinburg who were registered in Pharr
31 People voted in Edinburg who were registered in McAllen
2 People voted in Edinburg who were registered in La Joya
6 People voted in Edinburg who were registered in Edcouch
2 People voted in Edinburg who were registered in Mercedes
2 People voted in Edinburg who were registered in Monte Alto
6 People voted in Edinburg who were registered in Weslaco
1 Person voted in Edinburg who were registered in Penitas
3 People voted in Edinburg who were registered in Alamo
5 People voted in Edinburg who were registered in Elsa
6 People voted in Edinburg who were registered in Mission
1 Person voted in Edinburg who were registered in Alton

Will Esteban (9th Grade) Quintero CHEAT in 2020?

Only time will tell.

Vote Esteban (9th Grade) Quintero OUT of office.

```html
<!DOCTYPE html>
<html lang="en">
<head>
<meta charset="utf-8">
<title>Esteban (9th Grade) Quintero – Mail Piece</title>
<link href="https://fonts.googleapis.com/css2?family=Alfa+Slab+One&family=Khand:wght@400;600&family=Montserrat:wght@400;600;700;800&family=Open+Sans:wght@400;700&family=Oswald:wght@600;700&display=swap" rel="stylesheet">
<style>
  :root{
    --navy:#262c6b;
    --blue:#0b5aa8;
    --red:#e01e2b;
    --white:#ffffff;
    --page:#e9e9ea;
    --rule:#9a9a9a;
    --photo-a:#8a6a4a;
    --photo-b:#d8c2a8;
  }
  *{margin:0;padding:0;box-sizing:border-box}
  html,body{width:1068px;height:1200px;overflow:hidden;background:var(--page)}
  .canvas{position:relative;width:1068px;height:1200px}
  .card{position:absolute;left:173px;width:722px;height:486px;background:var(--white);overflow:hidden;box-shadow:0 2px 8px rgba(0,0,0,.18)}
  .card--front{top:160px}
  .card--back{top:676px}
  .layer{position:absolute;inset:0}

  /* front */
  .front-title{position:absolute;left:28px;top:18px}
  .front-photo{position:absolute;left:0;top:126px;width:722px;height:264px;
    background:linear-gradient(120deg,var(--photo-a),var(--photo-b) 55%,#7d7e80);
    clip-path:polygon(411px 0,722px 0,722px 264px,296px 264px)}
  .front-headline{position:absolute;left:30px;top:140px;color:var(--white);
    font:800 35px/1 "Montserrat",sans-serif;letter-spacing:.5px}
  .front-saying{position:absolute;left:28px;top:230px;width:320px;color:var(--white);
    font:400 18px/22px "Khand",sans-serif}
  .front-charge{position:absolute;left:27px;top:303px;width:290px;color:var(--white);
    font:400 14.5px/18px "Montserrat",sans-serif}
  .front-charge strong{font-weight:700}
  .phone{position:absolute;display:flex;align-items:center;gap:10px;color:var(--white);
    font:700 34px/1 "Montserrat",sans-serif;letter-spacing:-.5px}
  .front-phone{left:16px;top:421px}
  .front-vote{position:absolute;left:359px;top:409px}

  /* back */
  .back-question{position:absolute;left:23px;top:18px;color:var(--white);
    font:700 17.5px/20px "Montserrat",sans-serif}
  .back-intro{position:absolute;left:24px;top:95px;color:var(--white);
    font:600 17px/19px "Khand",sans-serif}
  .tally{position:absolute;left:23px;top:153px;list-style:none}
  .tally li{display:flex;align-items:center;gap:7px;height:15.5px;color:var(--white);
    font:400 11px/1 "Open Sans",sans-serif}
  .tally b{font-weight:700}
  .back-vote{position:absolute;left:19px;top:386px;color:var(--white);
    font:600 15.5px/1 "Montserrat",sans-serif}
  .back-phone{left:24px;top:433px;font-size:38px}
  .stamp-box{position:absolute;left:600px;top:31px;width:89px;height:102px;border:1.5px solid var(--rule)}
  .address-line{position:absolute;left:414px;width:273px;border-top:1px solid var(--rule)}
</style>
</head>
<body>
<div class="canvas">

  <!-- FRONT -->
  <section class="card card--front">
    <svg class="layer" width="722" height="486" viewBox="0 0 722 486">
      <polygon points="0,126 402,126 288,390 0,390" fill="var(--navy)"/>
      <polygon points="0,228 368,228 345,282 0,282" fill="var(--blue)"/>
      <polygon points="0,417 343,417 334,460 0,460" fill="var(--red)"/>
    </svg>
    <div class="front-photo" role="img" aria-label="Photo of two smiling men standing together, one in a white polo and one in a grey campaign polo"></div>

    <svg class="front-title" width="668" height="100" viewBox="0 0 668 100">
      <text x="0" y="74" textLength="664" lengthAdjust="spacingAndGlyphs"
        fill="var(--red)" font-family="'Alfa Slab One',serif" font-size="68">ESTEBAN(9TH GRADE)QUINTERO!</text>
    </svg>

    <h1 class="front-headline">WHAT'S THAT<br>FAMOUS SAYING?</h1>
    <p class="front-saying">Show me who your friends are and I'll tell you who you really are!</p>
    <p class="front-charge"><strong>Arturo Benavides</strong> is charged with voter fraud by changing voter addresses from across the RGV so they could vote in Edinburg</p>

    <div class="phone front-phone">
      <svg width="34" height="34" viewBox="0 0 34 34" aria-hidden="true">
        <circle cx="17" cy="17" r="15" fill="none" stroke="var(--white)" stroke-width="2.5"/>
        <path d="M12 9c1.5-1 2.5-.5 3 1l1 3c.3 1-.3 1.8-1.2 2.3 1 2.3 2.4 3.9 4.6 5 .6-.9 1.4-1.4 2.4-1l2.8 1.1c1.4.6 1.7 1.7.7 3-1.4 1.7-3.3 2-5.4 1-4.6-2.3-7.5-5.7-9-10.2-.7-2.1-.3-4 1.1-5.2z" fill="var(--white)"/>
      </svg>
      <span>1.234.567.8900</span>
    </div>

    <svg class="front-vote" width="342" height="66" viewBox="0 0 342 66">
      <text x="0" y="20" textLength="340" lengthAdjust="spacingAndGlyphs" font-family="'Oswald',sans-serif" font-weight="700" font-size="19" fill="var(--navy)">VOTE ESTEBAN <tspan fill="var(--red)">(9TH GRADE)</tspan> QUINTERO OUT OF OFFICE.</text>
      <text x="0" y="62" textLength="336" lengthAdjust="spacingAndGlyphs" font-family="'Oswald',sans-serif" font-weight="700" font-size="46" fill="var(--red)">ONLY TIME WILL TELL</text>
    </svg>
  </section>

  <!-- BACK -->
  <section class="card card--back">
    <svg class="layer" width="722" height="486" viewBox="0 0 722 486">
      <polygon points="0,0 311,0 418,486 0,486" fill="var(--navy)"/>
      <polygon points="311,0 323,0 430,486 418,486" fill="var(--red)"/>
      <polygon points="10,92 373,92 356,141 10,141" fill="var(--blue)"/>
      <polygon points="0,376 396,376 405,418 0,418" fill="var(--red)"/>
    </svg>

    <h2 class="back-question">Did Esteban (9th Grade)<br>Quintero commit voter fraud<br>when he ran for office in 2016?</h2>
    <p class="back-intro">Here is a list of people from all over the RGV that<br>voted in Edinburg in the 2016 race.</p>

    <ul class="tally">
      <li><svg width="12" height="12" viewBox="0 0 12 12" aria-hidden="true"><circle cx="6" cy="6" r="5" fill="none" stroke="var(--red)" stroke-width="1.3"/><path d="M3.4 6l2 2 4.2-5" fill="none" stroke="var(--red)" stroke-width="1.6"/></svg><span><b>9 People</b> voted in Edinburg who were registered in Donna.</span></li>
      <li><svg width="12" height="12" viewBox="0 0 12 12" aria-hidden="true"><circle cx="6" cy="6" r="5" fill="none" stroke="var(--red)" stroke-width="1.3"/><path d="M3.4 6l2 2 4.2-5" fill="none" stroke="var(--red)" stroke-width="1.6"/></svg><span><b>13 People</b> voted in Edinburg who were registered in San Juan</span></li>
      <li><svg width="12" height="12" viewBox="0 0 12 12" aria-hidden="true"><circle cx="6" cy="6" r="5" fill="none" stroke="var(--red)" stroke-width="1.3"/><path d="M3.4 6l2 2 4.2-5" fill="none" stroke="var(--red)" stroke-width="1.6"/></svg><span><b>8 People</b> voted in Edinburg who were registered in Pharr</span></li>
      <li><svg width="12" height="12" viewBox="0 0 12 12" aria-hidden="true"><circle cx="6" cy="6" r="5" fill="none" stroke="var(--red)" stroke-width="1.3"/><path d="M3.4 6l2 2 4.2-5" fill="none" stroke="var(--red)" stroke-width="1.6"/></svg><span><b>31 People</b> voted in Edinburg who were registered in McAllen</span></li>
      <li><svg width="12" height="12" viewBox="0 0 12 12" aria-hidden="true"><circle cx="6" cy="6" r="5" fill="none" stroke="var(--red)" stroke-width="1.3"/><path d="M3.4 6l2 2 4.2-5" fill="none" stroke="var(--red)" stroke-width="1.6"/></svg><span><b>2 People</b> voted in Edinburg who were registered in La Joya</span></li>
      <li><svg width="12" height="12" viewBox="0 0 12 12" aria-hidden="true"><circle cx="6" cy="6" r="5" fill="none" stroke="var(--red)" stroke-width="1.3"/><path d="M3.4 6l2 2 4.2-5" fill="none" stroke="var(--red)" stroke-width="1.6"/></svg><span><b>6 People</b> voted in Edinburg who were registered in Edcouch</span></li>
      <li><svg width="12" height="12" viewBox="0 0 12 12" aria-hidden="true"><circle cx="6" cy="6" r="5" fill="none" stroke="var(--red)" stroke-width="1.3"/><path d="M3.4 6l2 2 4.2-5" fill="none" stroke="var(--red)" stroke-width="1.6"/></svg><span><b>2 People</b> voted in Edinburg who were registered in Mercedes</span></li>
      <li><svg width="12" height="12" viewBox="0 0 12 12" aria-hidden="true"><circle cx="6" cy="6" r="5" fill="none" stroke="var(--red)" stroke-width="1.3"/><path d="M3.4 6l2 2 4.2-5" fill="none" stroke="var(--red)" stroke-width="1.6"/></svg><span><b>2 People</b> voted in Edinburg who were registered in Monte Alto</span></li>
      <li><svg width="12" height="12" viewBox="0 0 12 12" aria-hidden="true"><circle cx="6" cy="6" r="5" fill="none" stroke="var(--red)" stroke-width="1.3"/><path d="M3.4 6l2 2 4.2-5" fill="none" stroke="var(--red)" stroke-width="1.6"/></svg><span><b>6 People</b> voted in Edinburg who were registered in Weslaco</span></li>
      <li><svg width="12" height="12" viewBox="0 0 12 12" aria-hidden="true"><circle cx="6" cy="6" r="5" fill="none" stroke="var(--red)" stroke-width="1.3"/><path d="M3.4 6l2 2 4.2-5" fill="none" stroke="var(--red)" stroke-width="1.6"/></svg><span><b>1 Person</b> voted in Edinburg who were registered in Penitas</span></li>
      <li><svg width="12" height="12" viewBox="0 0 12 12" aria-hidden="true"><circle cx="6" cy="6" r="5" fill="none" stroke="var(--red)" stroke-width="1.3"/><path d="M3.4 6l2 2 4.2-5" fill="none" stroke="var(--red)" stroke-width="1.6"/></svg><span><b>3 People</b> voted in Edinburg who were registered in Alamo</span></li>
      <li><svg width="12" height="12" viewBox="0 0 12 12" aria-hidden="true"><circle cx="6" cy="6" r="5" fill="none" stroke="var(--red)" stroke-width="1.3"/><path d="M3.4 6l2 2 4.2-5" fill="none" stroke="var(--red)" stroke-width="1.6"/></svg><span><b>5 People</b> voted in Edinburg who were registered in Elsa</span></li>
      <li><svg width="12" height="12" viewBox="0 0 12 12" aria-hidden="true"><circle cx="6" cy="6" r="5" fill="none" stroke="var(--red)" stroke-width="1.3"/><path d="M3.4 6l2 2 4.2-5" fill="none" stroke="var(--red)" stroke-width="1.6"/></svg><span><b>6 People</b> voted in Edinburg who were registered in Mission</span></li>
      <li><svg width="12" height="12" viewBox="0 0 12 12" aria-hidden="true"><circle cx="6" cy="6" r="5" fill="none" stroke="var(--red)" stroke-width="1.3"/><path d="M3.4 6l2 2 4.2-5" fill="none" stroke="var(--red)" stroke-width="1.6"/></svg><span><b>1 Person</b> voted in Edinburg who were registered in Alton</span></li>
    </ul>

    <p class="back-vote">Vote Esteban (9th Grade) Quintero OUT of office.</p>

    <div class="phone back-phone">
      <svg width="40" height="40" viewBox="0 0 34 34" aria-hidden="true">
        <circle cx="17" cy="17" r="15" fill="none" stroke="var(--white)" stroke-width="2.5"/>
        <path d="M12 9c1.5-1 2.5-.5 3 1l1 3c.3 1-.3 1.8-1.2 2.3 1 2.3 2.4 3.9 4.6 5 .6-.9 1.4-1.4 2.4-1l2.8 1.1c1.4.6 1.7 1.7.7 3-1.4 1.7-3.3 2-5.4 1-4.6-2.3-7.5-5.7-9-10.2-.7-2.1-.3-4 1.1-5.2z" fill="var(--white)"/>
      </svg>
      <span>1.234.567.8900</span>
    </div>

    <div class="stamp-box"></div>
    <div class="address-line" style="top:193px"></div>
    <div class="address-line" style="top:240px"></div>
    <div class="address-line" style="top:287px"></div>
    <div class="address-line" style="top:332px"></div>
  </section>

</div>
</body>
</html>
```